Redesign of iOS App Lumo Tutor

Redesign of existing App Lumo Tutor, an app that helps learning Japanese Kanjis, Hiragana, Katakana.

The functionallity should remain the same as today: the app is free, you may download it at the app store. But: I like the design of my other apps better ;)

Target Market(s)

Students learning Japanese

Industry/Entity Type

Teacher

Font styles to use
Sans Serif

Requirements
Must have
• Lumo Tutor has 7 main screens, all screens has to be designed for iPhone and iPad: Main, Settings, Reading Tests, Writing Tests, Game, Paper Mode, Search
Nice to have
• I like the logo as it is today

```html
<!DOCTYPE html>
<html lang="en">
<head>
<meta charset="utf-8">
<title>Lumo Tutor – Kanji Detail</title>
<link rel="stylesheet" href="https://fonts.googleapis.com/css2?family=Roboto:wght@400;500;700&family=Noto+Sans+JP:wght@300;400;500&display=swap">
<style>
  :root {
    --bg: #ffffff;
    --status-bg: #f6f6f6;
    --ink: #1c1c1c;
    --muted: #8e8e8e;
    --faded: #c8c8c8;
    --rule: #d9d9d9;
    --blue: #4a90e2;
    --red: #b8192b;
    --teal: #17c1a8;
    --coral: #ef5a4c;
  }
  * { box-sizing: border-box; margin: 0; padding: 0; }
  html, body { width: 675px; height: 1200px; overflow: hidden; background: var(--bg); }
  body { position: relative; font-family: "Roboto", "Noto Sans JP", sans-serif; color: var(--ink); }

  .status-bar { position: absolute; left: 0; top: 0; width: 675px; height: 36px; background: var(--status-bg); font-size: 19px; }
  .status-bar .signal { position: absolute; left: 8px; top: 11px; display: flex; gap: 3px; align-items: center; }
  .status-bar .signal span { width: 9px; height: 9px; border-radius: 50%; background: var(--ink); }
  .status-bar .wifi { position: absolute; left: 88px; top: 8px; }
  .status-bar .time { position: absolute; left: 0; right: 0; top: 6px; text-align: center; font-weight: 500; }
  .status-bar .battery { position: absolute; right: 10px; top: 6px; display: flex; align-items: center; gap: 6px; }

  .detail-card { position: absolute; left: 40px; top: 60px; width: 594px; height: 943px; background: var(--bg); border-radius: 12px; box-shadow: 0 2px 14px rgba(0,0,0,0.12); }
  .headword { position: absolute; top: 28px; left: 0; right: 0; text-align: center; font-family: "Noto Sans JP", sans-serif; font-weight: 400; font-size: 92px; line-height: 1; letter-spacing: -2px; }
  .headword .known { color: var(--faded); font-weight: 300; }
  .headword-reading { position: absolute; top: 143px; left: 0; right: 0; text-align: center; font-family: "Noto Sans JP", sans-serif; font-size: 20px; color: var(--muted); }
  .headword-meaning { position: absolute; top: 171px; left: 0; right: 0; text-align: center; font-size: 19px; }
  .card-rule { position: absolute; top: 212px; left: 0; right: 0; height: 1px; background: var(--rule); }

  .row { position: absolute; left: 18px; right: 18px; font-size: 18px; line-height: 24px; height: 24px; }
  .row > span { position: absolute; top: 0; white-space: nowrap; }
  .kanji { left: 0; font-family: "Noto Sans JP", sans-serif; }
  .meaning { left: 41px; }
  .on { left: 202px; font-family: "Noto Sans JP", sans-serif; }
  .kun { left: 362px; font-family: "Noto Sans JP", sans-serif; }
  .level { right: 0; }
  .okurigana { color: var(--blue); }

  .section-title { position: absolute; left: 18px; right: 18px; display: flex; align-items: center; gap: 12px; font-size: 17.5px; color: var(--muted); line-height: 24px; }
  .section-title::before, .section-title::after { content: ""; flex: 1; height: 1px; background: var(--rule); }

  .example { position: absolute; left: 18px; right: 18px; font-size: 18px; }
  .example .word { position: absolute; left: 0; top: 0; font-family: "Noto Sans JP", sans-serif; }
  .example .kana { position: absolute; left: 202px; top: 0; font-family: "Noto Sans JP", sans-serif; }
  .example .gloss { position: absolute; left: 0; top: 24px; color: var(--blue); font-size: 19px; white-space: nowrap; }

  .legend { position: absolute; top: 1028px; font-size: 20px; display: flex; align-items: center; gap: 16px; }
  .legend .dot { width: 17px; height: 17px; border-radius: 50%; }
  .legend.correct { left: 120px; }
  .legend.correct .dot { background: var(--teal); }
  .legend.wrong { left: 459px; }
  .legend.wrong .dot { background: var(--coral); }

  .close-button { position: absolute; left: 299px; top: 982px; }
  .home-label { position: absolute; left: 0; right: 0; top: 1128px; text-align: center; font-size: 24px; font-weight: 700; }
</style>
</head>
<body>
  <header class="status-bar">
    <div class="signal"><span></span><span></span><span></span><span></span><span></span></div>
    <svg class="wifi" width="22" height="18" viewBox="0 0 22 18"><path d="M11 17 L7.5 13 A5 5 0 0 1 14.5 13 Z" fill="#1c1c1c"/><path d="M4 9.5 A10 10 0 0 1 18 9.5" stroke="#1c1c1c" stroke-width="2.4" fill="none"/><path d="M1 6 A14.5 14.5 0 0 1 21 6" stroke="#1c1c1c" stroke-width="2.4" fill="none"/></svg>
    <div class="time">9:41 AM</div>
    <div class="battery">100%
      <svg width="40" height="18" viewBox="0 0 40 18"><rect x="1" y="1" width="34" height="16" rx="3" fill="none" stroke="#1c1c1c" stroke-width="1.5"/><rect x="3" y="3" width="30" height="12" rx="1.5" fill="#1c1c1c"/><rect x="36.5" y="6" width="2.5" height="6" rx="1" fill="#1c1c1c"/></svg>
    </div>
  </header>

  <main class="detail-card">
    <div class="headword"><span class="known">外国</span>語</div>
    <div class="headword-reading">がいこくご</div>
    <div class="headword-meaning">foreign language</div>
    <div class="card-rule"></div>

    <div class="row" style="top:229px"><span class="kanji">語</span><span class="meaning">word</span><span class="on">ゴ</span><span class="level">N5</span></div>
    <div class="row" style="top:259px"><span class="on">かた<span class="okurigana">る</span>, かた<span class="okurigana">らう</span></span></div>

    <div class="section-title" style="top:312px">Non-trivial Components of Kanji 語</div>
    <div class="row" style="top:346px"><span class="kanji">言</span><span class="meaning">say</span><span class="on">ゲン, ゴン</span><span class="kun">い-, こと</span><span class="level">N5</span></div>
    <div class="row" style="top:378px"><span class="kanji">五</span><span class="meaning">five</span><span class="on">ゴ</span><span class="kun">いつ-</span><span class="level">N5</span></div>

    <div class="section-title" style="top:428px">Similar Pronunciation and in Group N5</div>
    <div class="row" style="top:461px"><span class="kanji">五</span><span class="meaning">five</span><span class="on">ゴ</span><span class="kun">いつ-</span><span class="level">N5</span></div>
    <div class="row" style="top:494px"><span class="kanji">午</span><span class="meaning">noon</span><span class="on">ゴ</span><span class="level">N5</span></div>
    <div class="row" style="top:527px"><span class="kanji">後</span><span class="meaning">behind</span><span class="on">ゴ, コウ</span><span class="kun">あと, うし-,…</span><span class="level">N5</span></div>

    <div class="section-title" style="top:576px">Example Words for 語 used in Tests</div>
    <div class="example" style="top:608px"><span class="word">言語</span><span class="kana">げんご</span><span class="gloss">language</span></div>
    <div class="example" style="top:674px"><span class="word">用語</span><span class="kana">ようご</span><span class="gloss">term, terminology</span></div>
    <div class="example" style="top:741px"><span class="word">外国語</span><span class="kana">がいこくご</span><span class="gloss">foreign language</span></div>
    <div class="example" style="top:806px"><span class="word">国語</span><span class="kana">こくご</span><span class="gloss">national language</span></div>
    <div class="example" style="top:873px"><span class="word">語る</span><span class="kana">かたる</span><span class="gloss">to talk about, to speak of, to tell, to narrate</span></div>
  </main>

  <div class="legend correct"><span class="dot"></span>Correct</div>
  <svg class="close-button" width="76" height="96" viewBox="0 0 76 96" role="button" aria-label="Close">
    <path d="M0 18 Q0 14 4 14 H30 L38 4 L46 14 H72 Q76 14 76 18 V58 A38 38 0 0 1 0 58 Z" fill="var(--red)"/>
    <path d="M27 39 L49 61 M49 39 L27 61" stroke="#fff" stroke-width="3" stroke-linecap="round"/>
  </svg>
  <div class="legend wrong"><span class="dot"></span>Wrong</div>

  <nav class="home-label">Home</nav>
</body>
</html>
```